Help keep hoosiers happy and at home!

We need a billboard designed for our Indiana based healthcare business called 'Willow Hearth Caregivers'. We administer a medicaid waiver program that provides support and financial aid to live in caregivers that take care of someone who would otherwise be in a nursing home or skilled nursing facility. Qualified caregivers could be eligible to receive up to 1200 dollars a month in tax free financial aid, as well as access to nursing support that helps manage any unexpected situations or changes in a care recipients condition or care routine. Our program empowers families to keep their loved ones at home and out of the nursing home. NOTE: We believe the tagline at the bottom of our logo is disproportionately small. We would like to see that tagline larger and easier to read. I look forward to seeing your design ideas!

Target Market(s)

Medicaid aged beneficiaries and caregivers.

Industry/Entity Type

Home Healthcare

Colors
0054AA
0677BA
7BADD7
CADEEF
E8F1F8

Requirements
Nice to have
• "Empowering friends and family to care for their loves ones at home. Eligible participants receive up to $15,000 a year, tax free."

```html
<!DOCTYPE html>
<html lang="en">
<head>
<meta charset="utf-8">
<title>Willow Hearth Caregivers – Billboard</title>
<link href="https://fonts.googleapis.com/css2?family=Montserrat:wght@400;500;700&display=swap" rel="stylesheet">
<style>
  :root {
    --page-bg: #ffffff;
    --panel-light-start: #dfe3f4;
    --panel-light-end: #ffffff;
    --house-blue: #1b75bc;
    --navy-start: #232766;
    --navy-end: #2f3577;
    --text-navy: #2a2f6f;
    --text-blue: #1b75bc;
    --text-light: #ffffff;
  }
  * { box-sizing: border-box; margin: 0; padding: 0; }
  html, body {
    width: 1200px;
    height: 1118px;
    overflow: hidden;
    background: var(--page-bg);
    font-family: "Montserrat", sans-serif;
  }
  .billboard {
    position: absolute;
    left: 40px;
    top: 395px;
    width: 1120px;
    height: 327px;
    overflow: hidden;
  }
  .billboard__shapes {
    position: absolute;
    inset: 0;
    width: 100%;
    height: 100%;
  }
  .message {
    position: absolute;
    left: 46px;
    top: 44px;
    color: var(--text-navy);
    font-size: 26.5px;
    line-height: 34px;
    font-weight: 400;
  }
  .message strong { color: var(--text-blue); font-weight: 700; }
  .website {
    position: absolute;
    left: 46px;
    top: 250px;
    font-size: 16px;
    color: var(--text-blue);
  }
  .website strong { font-weight: 700; }
  .brand-name {
    position: absolute;
    left: 371px;
    width: 378px;
    top: 205px;
    text-align: center;
    color: var(--text-light);
    font-weight: 500;
    font-size: 24px;
    line-height: 30px;
    letter-spacing: 2px;
  }
  .offer {
    position: absolute;
    right: 46px;
    top: 44px;
    text-align: right;
    color: var(--text-light);
    font-size: 26.5px;
    line-height: 34px;
  }
  .offer__amount {
    display: block;
    font-size: 56px;
    line-height: 62px;
    font-weight: 700;
  }
  .offer strong { font-weight: 700; }
  .contact {
    position: absolute;
    right: 46px;
    top: 248px;
    text-align: right;
    color: var(--text-light);
  }
  .contact__label { font-size: 16px; line-height: 20px; }
  .contact__phone { font-size: 38px; line-height: 42px; font-weight: 700; }
</style>
</head>
<body>
  <section class="billboard">
    <svg class="billboard__shapes" viewBox="0 0 1120 327" preserveAspectRatio="none" aria-hidden="true">
      <defs>
        <linearGradient id="lightPanel" x1="0" y1="0" x2="1" y2="0.6">
          <stop offset="0" stop-color="#dfe3f4"/>
          <stop offset="0.35" stop-color="#ffffff"/>
          <stop offset="1" stop-color="#ffffff"/>
        </linearGradient>
        <linearGradient id="navyPanel" x1="0" y1="0" x2="1" y2="1">
          <stop offset="0" stop-color="#232766"/>
          <stop offset="1" stop-color="#2f3577"/>
        </linearGradient>
      </defs>
      <rect class="panel-light" x="0" y="0" width="1120" height="327" fill="url(#lightPanel)"/>
      <polygon class="panel-navy" points="560,0 1120,0 1120,327 749,327 749,173 796,173" fill="url(#navyPanel)"/>
      <polygon class="house-panel" points="560,0 796,173 749,173 749,327 371,327 371,173 323,173" fill="#1b75bc"/>
    </svg>

    <p class="message">Empowering<br><strong>friends and family</strong> to care<br>for their loves ones<br>at home</p>
    <p class="website"><strong>willowhearth</strong>caregivers.com</p>

    <p class="brand-name">Willow Hearth<br>Caregivers</p>

    <p class="offer">Eligible participants<br>receive up to<span class="offer__amount">$15,000</span><strong>a year</strong>, tax free.</p>

    <div class="contact">
      <p class="contact__label">Call us today at</p>
      <p class="contact__phone">(800)555-0142</p>
    </div>
  </section>
</body>
</html>
```